Redesigned PowerPoint template for Restaurant Services Company

We need a redesigned company template for powerpoints. looking for something modern and easy to use. If we like it, we will add additional products for the design (letterhead, social media banners, etc).

Target Market(s)

restaurant owners, and franchise owners

Font styles to use
Serif
Sans Serif

Colors
0355a3
f0474d
ffffff

Requirements
Must have
• - something that uses our colors in a modern way
- easy to use
- something that is eye catching
Nice to have
• - multiple slide types (picture and text, graphic and text, bulleted text, etc)
- easy way to swap out our prospects logo and have our prospects logo displayed throughout the deck
Should not have
• should not have locked or anchored fields making it difficult to edit

```html
<!DOCTYPE html>
<html lang="en">
<head>
<meta charset="utf-8">
<title>Sample Slides</title>
<link href="https://fonts.googleapis.com/css2?family=Montserrat:wght@400;600;700;800&family=Merriweather:wght@400;700&display=swap" rel="stylesheet">
<style>
  :root{
    --blue:#0355a3;
    --navy:#12284a;
    --red:#f0474d;
    --deep-red:#c9252c;
    --white:#ffffff;
    --ink:#2a2f3a;
    --muted:#7d8594;
    --rule:#e2e6ee;
    --page:#f1f2f4;
  }
  *{margin:0;padding:0;box-sizing:border-box;}
  html,body{width:742px;height:1200px;overflow:hidden;background:var(--page);}
  body{font-family:"Montserrat",Arial,sans-serif;color:var(--ink);position:relative;}
  .sheet-title{position:absolute;top:20px;left:0;width:742px;text-align:center;font-weight:800;font-size:30px;color:var(--navy);letter-spacing:-0.5px;}
  .sheet-title span{color:var(--red);}
  .slide{position:absolute;width:318px;height:180px;background:var(--white);overflow:hidden;box-shadow:0 1px 4px rgba(0,0,0,.18);}
  .col-a{left:40px;} .col-b{left:384px;}
  .row-1{top:86px;} .row-2{top:298px;} .row-3{top:510px;} .row-4{top:722px;} .row-5{top:934px;}
  .brand{position:absolute;display:flex;align-items:center;gap:4px;font-weight:800;color:var(--blue);font-size:8px;letter-spacing:.5px;}
  .brand i{display:block;width:9px;height:9px;background:var(--red);}
  .brand.light{color:var(--white);}
  .slide-head{position:absolute;left:14px;top:30px;font-size:8px;font-weight:800;color:var(--blue);letter-spacing:.3px;}
  .head-rule{position:absolute;left:14px;top:42px;width:26px;height:2px;background:var(--red);}
  .footer{position:absolute;left:0;bottom:0;width:100%;height:14px;border-top:1px solid var(--rule);background:var(--white);}
  .footer .url{position:absolute;left:14px;top:4px;font-size:4.5px;color:var(--muted);}
  .footer .num{position:absolute;right:10px;top:2px;width:10px;height:10px;background:var(--blue);color:var(--white);font-size:5px;text-align:center;line-height:10px;}
  .small{font-size:5px;line-height:1.5;color:var(--ink);}
  .bullets{list-style:none;}
  .bullets li{position:relative;padding-left:7px;margin-bottom:5px;font-size:5px;line-height:1.3;}
  .bullets li::before{content:"";position:absolute;left:0;top:2px;width:3px;height:3px;background:var(--red);}
  .photo{position:absolute;}
  .serif{font-family:"Merriweather",Georgia,serif;}
  .label{position:absolute;font-size:5px;text-align:center;color:var(--ink);line-height:1.4;}
  .label b{display:block;font-weight:700;}
  svg{position:absolute;}
</style>
</head>
<body>

<h1 class="sheet-title">Sample <span>Slides</span></h1>

<!-- Cover -->
<section class="slide col-a row-1" style="background:var(--red);">
  <svg width="318" height="180" viewBox="0 0 318 180">
    <polygon points="0,0 110,0 60,180 0,180" fill="var(--deep-red)" opacity=".55"/>
    <polygon points="250,180 318,110 318,180" fill="var(--navy)" opacity=".35"/>
  </svg>
  <div class="brand light" style="left:40px;top:78px;font-size:13px;"><i style="width:14px;height:14px;background:var(--white);"></i>BRIGHTLINE</div>
  <div style="position:absolute;left:58px;top:96px;font-size:5px;color:var(--white);letter-spacing:1.5px;">HOSPITALITY GROUP</div>
</section>

<!-- Overview -->
<section class="slide col-b row-1">
  <div class="photo" role="img" aria-label="Restaurant dining room photo with blue tint" style="left:70px;top:0;width:248px;height:180px;background:linear-gradient(135deg,#2b4f86,#0d2a55);"></div>
  <svg width="318" height="180" viewBox="0 0 318 180">
    <polygon points="0,0 110,0 70,180 0,180" fill="var(--white)"/>
    <polygon points="110,0 122,0 82,180 70,180" fill="var(--red)"/>
    <rect x="100" y="150" width="218" height="30" fill="var(--blue)" opacity=".9"/>
  </svg>
  <div class="brand" style="left:14px;top:14px;"><i></i>BRIGHTLINE</div>
  <div style="position:absolute;left:130px;top:72px;font-size:15px;font-weight:700;color:var(--white);">BHG Overview 2021</div>
  <div style="position:absolute;left:240px;top:156px;font-size:4.5px;color:var(--white);line-height:1.4;">Prepared by<br><b style="font-size:6px;">Jordan Vale</b></div>
</section>

<!-- At a glance -->
<section class="slide col-a row-2">
  <div class="brand" style="left:14px;top:10px;"><i></i>BRIGHTLINE</div>
  <div class="slide-head">BHG AT A GLANCE</div><div class="head-rule"></div>
  <ul class="bullets" style="position:absolute;left:14px;top:54px;width:150px;">
    <li>Founded and based in Austin, TX in 2011</li>
    <li>Owner-operated approach</li>
    <li>Marketing, construction and managed operations services</li>
    <li>Experienced team of restaurant operators</li>
    <li>Proprietary technology platform across all properties</li>
    <li>Successfully managed over 40 locations in five states</li>
    <li>Over 70 000 hours of hands-on support</li>
  </ul>
  <div class="photo" role="img" aria-label="State map with highlighted office locations" style="left:186px;top:56px;width:100px;height:84px;background:linear-gradient(160deg,#2f6fb8,#0355a3);border-radius:4px;"></div>
  <div class="footer"><span class="url">brightlinehospitality.com</span><span class="num">3</span></div>
</section>

<!-- Stand for -->
<section class="slide col-b row-2">
  <div class="brand" style="left:14px;top:10px;"><i></i>BRIGHTLINE</div>
  <div class="slide-head">WHAT WE STAND FOR</div><div class="head-rule"></div>
  <div style="position:absolute;left:14px;top:52px;width:290px;height:96px;background:var(--blue);"></div>
  <p class="serif" style="position:absolute;left:34px;top:60px;width:250px;font-size:5.5px;line-height:1.5;color:var(--white);text-align:center;">"We believe in giving every owner the tools, people and clarity to grow a restaurant they are proud of, one guest at a time, one shift at a time."</p>
  <div class="photo" role="img" aria-label="Round portrait of company founder" style="left:146px;top:92px;width:26px;height:26px;border-radius:50%;background:linear-gradient(#9fb6d6,#5c7fae);border:1.5px solid var(--white);"></div>
  <div style="position:absolute;left:0;width:318px;top:124px;text-align:center;font-size:5px;color:var(--white);font-weight:700;line-height:1.4;">Sam Harlow<br><span style="font-weight:400;">Founder</span></div>
  <div class="footer"><span class="url">brightlinehospitality.com</span><span class="num">4</span></div>
</section>

<!-- What we do -->
<section class="slide col-a row-3">
  <div class="photo" role="img" aria-label="Photo of hands writing plans at a desk" style="left:0;top:0;width:318px;height:180px;background:linear-gradient(120deg,#c9c3b8,#6d6a66);"></div>
  <div style="position:absolute;left:150px;top:32px;width:140px;height:110px;background:var(--blue);opacity:.93;"></div>
  <div style="position:absolute;left:150px;top:32px;width:4px;height:110px;background:var(--red);"></div>
  <div style="position:absolute;left:164px;top:44px;font-size:9px;font-weight:800;color:var(--white);">WHAT WE DO</div>
  <p style="position:absolute;left:164px;top:62px;width:116px;font-size:5px;line-height:1.5;color:var(--white);">Brightline is an independent restaurant services firm offering consulting, marketing, technology, construction and dedicated managed operations services. We deliver results that move the needle.</p>
</section>

<!-- Moving the needle -->
<section class="slide col-b row-3">
  <div class="brand" style="left:14px;top:10px;"><i></i>BRIGHTLINE</div>
  <div style="position:absolute;left:130px;top:30px;font-size:8px;font-weight:800;color:var(--blue);">MOVING THE NEEDLE WITH BHG360</div>
  <div style="position:absolute;left:130px;top:42px;width:26px;height:2px;background:var(--red);"></div>
  <div class="photo" role="img" aria-label="Illustration of a target with darts" style="left:16px;top:36px;width:100px;height:100px;border-radius:6px;background:linear-gradient(145deg,#f4f5f8,#e3e7ee);"></div>
  <div style="position:absolute;left:130px;top:52px;width:170px;">
    <div style="font-size:5.5px;font-weight:700;color:var(--red);margin-bottom:3px;">Operational Efficiency</div>
    <ul class="bullets"><li>Proven systems that lower costs and raise guest scores</li><li>Shared purchasing power for every location</li></ul>
    <div style="font-size:5.5px;font-weight:700;color:var(--red);margin:2px 0 3px;">Reduced Costs</div>
    <ul class="bullets"><li>Smart labor and food cost planning</li><li>Clear monthly reporting</li></ul>
    <div style="font-size:5.5px;font-weight:700;color:var(--red);margin:2px 0 3px;">New and Increased Revenue</div>
    <ul class="bullets"><li>Local marketing, catering and online ordering</li></ul>
  </div>
  <div class="footer"><span class="url">brightlinehospitality.com</span><span class="num">6</span></div>
</section>

<!-- Value steps -->
<section class="slide col-a row-4">
  <div class="brand" style="left:14px;top:10px;"><i></i>BRIGHTLINE</div>
  <div style="position:absolute;left:14px;top:28px;font-size:9px;font-weight:800;color:var(--red);">BHG Value(s)</div>
  <svg width="318" height="180" viewBox="0 0 318 180">
    <polygon points="10,166 260,40 300,40 300,166" fill="#eef2f8"/>
    <g font-family="Montserrat,Arial,sans-serif" font-weight="700" font-size="7" fill="#ffffff" text-anchor="middle">
      <circle cx="50" cy="138" r="12" fill="var(--blue)"/><text x="50" y="141">01</text>
      <circle cx="100" cy="115" r="12" fill="var(--navy)"/><text x="100" y="118">02</text>
      <circle cx="150" cy="92" r="12" fill="var(--red)"/><text x="150" y="95">03</text>
      <circle cx="200" cy="69" r="12" fill="var(--blue)"/><text x="200" y="72">04</text>
      <circle cx="250" cy="46" r="12" fill="var(--deep-red)"/><text x="250" y="49">05</text>
    </g>
    <g font-family="Montserrat,Arial,sans-serif" font-size="5" fill="var(--ink)" font-weight="700">
      <text x="26" y="160">Assessment</text>
      <text x="76" y="138">Strategy</text>
      <text x="126" y="115">Set-up</text>
      <text x="176" y="92">Launch</text>
      <text x="226" y="70">Results</text>
    </g>
  </svg>
  <div class="footer"><span class="url">brightlinehospitality.com</span><span class="num">7</span></div>
</section>

<!-- Value map -->
<section class="slide col-b row-4">
  <div class="brand" style="left:14px;top:10px;"><i></i>BRIGHTLINE</div>
  <div class="photo" role="img" aria-label="Illustration of a winding road with milestone markers" style="left:20px;top:56px;width:278px;height:98px;border-radius:8px;background:linear-gradient(180deg,#4a4f5a,#2e323b);"></div>
  <div style="position:absolute;left:20px;top:98px;width:278px;text-align:center;font-size:10px;font-weight:800;color:var(--white);">BHG Value Map</div>
  <div class="label" style="left:30px;top:34px;width:100px;"><b style="color:var(--blue);">Alignment</b>Shared goals from day one</div>
  <div class="label" style="left:180px;top:34px;width:100px;"><b style="color:var(--red);">Priorities</b>Focus on what matters most</div>
  <div class="label" style="left:70px;top:160px;width:100px;"><b style="color:var(--blue);">Execution</b></div>
  <div class="label" style="left:190px;top:160px;width:100px;"><b style="color:var(--red);">Commitment</b></div>
</section>

<!-- Execution services -->
<section class="slide col-a row-5">
  <div class="brand" style="left:14px;top:10px;"><i></i>BRIGHTLINE</div>
  <svg width="318" height="180" viewBox="0 0 318 180">
    <g stroke="var(--red)" stroke-width="1.2" fill="none">
      <path d="M120,90 C100,90 100,40 70,40"/>
      <path d="M120,90 C100,90 100,70 70,70"/>
      <path d="M120,90 C100,90 100,110 70,110"/>
      <path d="M120,90 C100,90 100,140 70,140"/>
      <path d="M198,90 C218,90 218,40 248,40"/>
      <path d="M198,90 C218,90 218,70 248,70"/>
      <path d="M198,90 C218,90 218,110 248,110"/>
      <path d="M198,90 C218,90 218,140 248,140"/>
    </g>
    <rect x="120" y="70" width="78" height="40" fill="var(--blue)"/>
    <g font-family="Montserrat,Arial,sans-serif" font-size="6.5" font-weight="700" fill="#ffffff" text-anchor="middle">
      <text x="159" y="88">BHG Execution</text>
      <text x="159" y="97">Services</text>
    </g>
    <g font-family="Montserrat,Arial,sans-serif" font-size="5" fill="var(--ink)" font-weight="600">
      <text x="14" y="42">Restaurant Mgmt</text>
      <text x="14" y="72">Marketing</text>
      <text x="14" y="112">Design &amp; Build</text>
      <text x="14" y="142">Growth Planning</text>
      <text x="252" y="42">Technology</text>
      <text x="252" y="72">Purchasing</text>
      <text x="252" y="112">Training</text>
      <text x="252" y="142">Reporting</text>
    </g>
  </svg>
  <div class="footer"><span class="url">brightlinehospitality.com</span><span class="num">9</span></div>
</section>

<!-- Restaurant services -->
<section class="slide col-b row-5">
  <div class="photo" role="img" aria-label="Photo of a plated restaurant dish" style="left:0;top:0;width:130px;height:180px;background:linear-gradient(150deg,#8a6a4f,#3b2c22);"></div>
  <div style="position:absolute;left:0;top:128px;width:130px;height:38px;background:var(--red);"></div>
  <div style="position:absolute;left:12px;top:135px;font-size:8px;font-weight:800;color:var(--white);line-height:1.25;">RESTAURANT<br>SERVICES</div>
  <div class="brand" style="left:244px;top:10px;"><i></i>BRIGHTLINE</div>
  <div style="position:absolute;left:146px;top:34px;width:160px;">
    <div style="font-size:5.5px;font-weight:700;color:var(--blue);margin-bottom:2px;">New Restaurant Consulting</div>
    <p class="small" style="margin-bottom:6px;">Concept development, site selection, menu planning and opening support.</p>
    <div style="font-size:5.5px;font-weight:700;color:var(--blue);margin-bottom:2px;">Existing Restaurant Consulting</div>
    <p class="small" style="margin-bottom:6px;">Operational review, cost controls, staffing plans and service training.</p>
    <div style="font-size:5.5px;font-weight:700;color:var(--blue);margin-bottom:2px;">Franchise Support</div>
    <p class="small">Multi-unit rollout, brand standards and owner reporting for growing groups.</p>
  </div>
</section>

</body>
</html>
```